依頼詳細
お好み焼き屋さんのTOPページのみのデザインをお願いしたいです。
コロナで減少したお客様を呼び戻すために試行錯誤しながら、このたびラーメンも提供することになりましたので、メインはお好み焼き屋さんですが、ラーメンも始めました!という画像付きで告知したいです。

集客を目的としたサイトです。
ターゲットは。お腹が空いた人になります!

レイアウト構成
・ヘッダー(ロゴのみ)
・TOP画像(画像はまだないのでフリーのもので大丈夫です)
・TOPページは画像だけでなくインパクトある感じを希望です(ザックリですみません。)
・お知らせ(3行程度)
・メニュー(テキストのみ)
・店舗情報(2店舗)テキスト
・フッター(下層ページないのでコピーライトぐらいでしょうか)
という構成です。
どこかにツマミドリと味ノートにリンクするボタンが欲しいです。
まだ素材がないため仮のフリー画像で構いません。

初心者の方でも大丈夫です!
今回は予算の都合上、低価格になってしまいましたがデザインのフィーリングが合う方は今後もご依頼する可能性があります!
サイトURL
ページ数
1ページ
希望イメージ
シンプル 複雑
単色 カラフル
暗い 明るい
日常 高級
遊び心 厳粛
未来的 伝統的
女性的 男性的
希望する色
無彩色系
納品ファイル
• 高解像度JPG (.jpg)
• イラストレーター形式 (.ai)
• フォトショップ形式 (.psd)
• PNG形式 (.png)
補足説明
納品はできれば、XDが希望です。
難しい場合はご相談ください。

お客様のイメージに一番近かったため選びました!

この度は、とても素晴らしいデザインのご提案をいただきまして誠にありがとうございました。
どれも捨てがたいデザインなのですが、一番イメージに近いものを選びました。
また、機会がございましたら、ご依頼をさせていただければと思います。
どうぞよろしくお願いいたします。

```html
<!DOCTYPE html>
<html lang="ja">
<head>
<meta charset="UTF-8">
<title>お好み焼き鉄平</title>
<link href="https://fonts.googleapis.com/css2?family=Shippori+Mincho+B1:wght@400;700;800&family=Yuji+Boku&display=swap" rel="stylesheet">
<style>
:root{
  --wood-dark:#1e130b;
  --wood:#3a2616;
  --wood-mid:#4a3120;
  --olive:#7d7a22;
  --olive-dark:#5c5a15;
  --olive-light:#a19d35;
  --gold:#d9c74a;
  --cream:#f1ead6;
  --text:#e9e2cf;
  --panel:rgba(120,110,80,.28);
  --footer:#2c2c14;
}
*{margin:0;padding:0;box-sizing:border-box}
html,body{width:1200px;height:3692px;overflow:hidden}
body{
  position:relative;
  font-family:"Shippori Mincho B1",serif;
  color:var(--text);
  background:
    repeating-linear-gradient(90deg,rgba(0,0,0,.18) 0 3px,transparent 3px 38px,rgba(255,255,255,.03) 38px 40px,transparent 40px 90px),
    linear-gradient(180deg,var(--wood-mid),var(--wood) 40%,var(--wood-dark));
}
.abs{position:absolute}
/* header */
.site-header{left:0;top:0;width:1200px;height:64px;display:flex;align-items:center;justify-content:space-between;padding:0 32px;background:rgba(20,12,6,.55)}
.logo{font-family:"Yuji Boku",serif;font-size:26px;color:var(--cream);letter-spacing:.04em}
.nav{display:flex;align-items:center;gap:26px;font-size:14px}
.nav a{color:var(--text);text-decoration:none}
.btn-pill{display:inline-block;border-radius:30px;padding:7px 22px;font-size:13px;font-weight:700;text-decoration:none}
.btn-outline{border:1px solid var(--gold);color:var(--gold)!important}
.btn-solid{background:var(--gold);color:#2a1c0c!important}
/* hero */
.hero-photo{left:0;top:64px;width:540px;height:380px;background:radial-gradient(ellipse at 45% 55%,#b8622c,#7a3b1a 55%,#2b170c);clip-path:polygon(0 0,100% 0,96% 70%,70% 100%,0 96%)}
.hero-copy{left:780px;top:90px;height:260px;writing-mode:vertical-rl;font-family:"Yuji Boku",serif;font-size:34px;line-height:1.3;color:var(--cream)}
.hero-title{left:880px;top:300px;writing-mode:vertical-rl;font-family:"Yuji Boku",serif;font-size:88px;line-height:1.05;color:var(--cream);letter-spacing:.02em}
.hero-title span{display:block}
.ramen-photo{left:700px;top:520px;width:300px;height:210px;border-radius:6px;background:radial-gradient(circle at 50% 50%,#d9b27a,#8c5a2c 55%,#2a1c10)}
.ramen-head{left:170px;top:630px;font-family:"Yuji Boku",serif;font-size:54px;color:var(--gold)}
.ramen-text{left:180px;top:718px;font-size:17px;line-height:1.8;color:var(--cream)}
/* news */
.news{left:180px;top:920px;width:840px;height:460px;background:var(--panel);border:1px solid rgba(200,190,130,.3);padding:40px 60px}
.news h2{text-align:center;font-size:24px;margin-bottom:34px;color:var(--cream)}
.news-list li{list-style:none;display:flex;gap:40px;font-size:13px;padding:16px 10px;border-bottom:1px solid rgba(220,210,170,.25)}
.news-list time{color:var(--gold)}
.news-btns{position:absolute;left:0;right:0;bottom:50px;display:flex;justify-content:center;gap:40px}
.news-btns a{width:220px;text-align:center;background:var(--olive);color:var(--cream);border-radius:30px;padding:12px 0;font-size:13px;text-decoration:none}
/* section heading */
.sec-title{left:0;width:1200px;text-align:center;font-size:30px;font-weight:700;color:var(--cream)}
.sec-title::before,.sec-title::after{content:"";display:inline-block;width:100px;height:1px;background:var(--olive-light);vertical-align:middle;margin:0 24px}
/* menu tags */
.tag{width:92px;height:330px;background:linear-gradient(180deg,var(--olive-light),var(--olive) 40%,var(--olive-dark));border:2px solid #3b3a10;box-shadow:0 4px 10px rgba(0,0,0,.5);display:flex;flex-direction:row-reverse;justify-content:center;gap:10px;padding-top:34px}
.tag::before{content:"";position:absolute;top:10px;left:50%;width:10px;height:10px;margin-left:-5px;border-radius:50%;background:var(--wood-dark)}
.tag-name{writing-mode:vertical-rl;font-size:26px;font-weight:800;color:var(--cream);letter-spacing:.08em}
.tag-price{writing-mode:vertical-rl;font-size:12px;color:var(--cream);margin-top:auto;padding-bottom:18px}
.cat-label{writing-mode:vertical-rl;font-family:"Yuji Boku",serif;font-size:42px;color:var(--gold)}
/* shops */
.shop{top:2720px;width:440px;height:520px;background:var(--panel);border:1px solid rgba(200,190,130,.3);padding:26px}
.map{width:388px;height:260px;background:linear-gradient(135deg,#cfc9b2,#a9b29a 50%,#c7b994);border-radius:2px}
.shop h3{text-align:center;font-size:22px;margin:22px 0 16px;color:var(--cream)}
.shop dl{display:grid;grid-template-columns:90px 1fr;row-gap:10px;font-size:13px}
.shop dt{color:var(--gold)}
/* footer */
.site-footer{left:0;top:3370px;width:1200px;height:322px;background:var(--footer);text-align:center;padding-top:80px}
.site-footer .logo{font-size:36px}
.foot-nav{display:flex;justify-content:center;gap:36px;margin-top:50px;font-size:13px}
.foot-nav a{color:var(--text);text-decoration:none}
.copy{margin-top:30px;font-size:11px;color:#b8b08a}
</style>
</head>
<body>

<header class="site-header abs">
  <div class="logo">お好み焼き鉄平</div>
  <nav class="nav">
    <a href="#">TOP</a><a href="#">メニュー</a><a href="#">店舗情報</a>
    <a class="btn-pill btn-outline" href="#">ツマミドリ</a>
    <a class="btn-pill btn-solid" href="#">味ノート</a>
  </nav>
</header>

<div class="hero-photo abs" role="img" aria-label="鉄板で焼き上がった豚玉お好み焼きの写真"></div>
<p class="hero-copy abs">ふわふわの生地に<br>ジューシーな豚肉のうまみ</p>
<h1 class="hero-title abs"><span>絶品</span><span>豚玉</span></h1>
<div class="ramen-photo abs" role="img" aria-label="豚骨ラーメンの写真"></div>
<h2 class="ramen-head abs">ラーメン始めました</h2>
<p class="ramen-text abs">食べた瞬間、口いっぱいに広がる豚骨と野菜の香り！<br>ぜひ一度お試しください。</p>

<section class="news abs">
  <h2>お知らせ</h2>
  <ul class="news-list">
    <li><time>2021.03.15</time>ランチタイムメニューが新しくなりました</li>
    <li><time>2021.03.01</time>新メニュー「特製しょうゆラーメン」を始めました</li>
    <li><time>2021.02.20</time>臨時休業のお知らせ</li>
  </ul>
  <div class="news-btns"><a href="#">ツマミドリで予約</a><a href="#">味ノートで見る</a></div>
</section>

<h2 class="sec-title abs" style="top:1510px">おしながき</h2>

<div class="abs tag" style="left:106px;top:1620px"><span class="tag-name">スペシャル</span><span class="tag-price">1,200円（税込）</span></div>
<div class="abs tag" style="left:220px;top:1620px"><span class="tag-name">海鮮ミックス玉</span><span class="tag-price">1,100円（税込）</span></div>
<div class="abs tag" style="left:334px;top:1620px"><span class="tag-name">えび玉</span><span class="tag-price">900円（税込）</span></div>
<div class="abs tag" style="left:448px;top:1620px"><span class="tag-name">いか玉</span><span class="tag-price">850円（税込）</span></div>
<div class="abs tag" style="left:562px;top:1620px"><span class="tag-name">牛玉</span><span class="tag-price">950円（税込）</span></div>
<div class="abs tag" style="left:676px;top:1620px"><span class="tag-name">ミックス玉</span><span class="tag-price">1,000円（税込）</span></div>
<div class="abs tag" style="left:790px;top:1620px"><span class="tag-name">豚キムチ</span><span class="tag-price">900円（税込）</span></div>
<div class="abs tag" style="left:904px;top:1620px"><span class="tag-name">絶品豚玉</span><span class="tag-price">850円（税込）</span></div>
<div class="abs cat-label" style="left:1040px;top:1620px">お好み焼き</div>

<div class="abs cat-label" style="left:200px;top:2090px">ラーメン</div>
<div class="abs tag" style="left:258px;top:2040px"><span class="tag-name">特製しょうゆ</span><span class="tag-price">800円（税込）</span></div>
<div class="abs tag" style="left:420px;top:2040px"><span class="tag-name">スペシャル</span><span class="tag-price">1,200円（税込）</span></div>
<div class="abs tag" style="left:534px;top:2040px"><span class="tag-name">海鮮ミックス</span><span class="tag-price">1,100円（税込）</span></div>
<div class="abs tag" style="left:648px;top:2040px"><span class="tag-name">明太チーズ</span><span class="tag-price">1,000円（税込）</span></div>
<div class="abs tag" style="left:762px;top:2040px"><span class="tag-name">豚キムチ</span><span class="tag-price">950円（税込）</span></div>
<div class="abs tag" style="left:876px;top:2040px"><span class="tag-name">ミックス</span><span class="tag-price">900円（税込）</span></div>
<div class="abs cat-label" style="left:1000px;top:2090px">もんじゃ焼き</div>

<h2 class="sec-title abs" style="top:2600px">店舗情報</h2>

<section class="shop abs" style="left:130px">
  <div class="map" role="img" aria-label="千駄ヶ谷店周辺の地図"></div>
  <h3>千駄ヶ谷店</h3>
  <dl>
    <dt>住所</dt><dd>〒151-0000 東京都渋谷区鉄板町1-2-3</dd>
    <dt>電話番号</dt><dd>03-0000-1234</dd>
    <dt>営業時間</dt><dd>11:00〜22:00</dd>
  </dl>
</section>
<section class="shop abs" style="left:630px">
  <div class="map" role="img" aria-label="神戸三宮店周辺の地図"></div>
  <h3>神戸三宮店</h3>
  <dl>
    <dt>住所</dt><dd>〒650-0000 兵庫県神戸市中央区鉄板通4-5-6</dd>
    <dt>電話番号</dt><dd>078-000-5678</dd>
    <dt>営業時間</dt><dd>11:00〜22:00</dd>
  </dl>
</section>

<footer class="site-footer abs">
  <div class="logo">お好み焼き鉄平</div>
  <nav class="foot-nav"><a href="#">TOP</a><a href="#">メニュー</a><a href="#">店舗情報</a><a href="#">ツマミドリ</a><a href="#">味ノート</a></nav>
  <p class="copy">© Okonomiyaki Teppei. All Rights Reserved.</p>
</footer>

</body>
</html>
```